Hedge Fund Business Presentation for prospective clients

We need a professional design for our PowerPoint presentation that we use to send to prospective clients for our Alternative Investments/Hedge Fund. This presentation needs to have the same verbiage as what is being used already. We will present this to individuals, institutions (banks, non profits), and to Registered Investment Advisors that have client money to place.

Target Market(s)

High net worth individuals, high income earners, doctors, lawyers, business owners, sophisticated investors

Industry/Entity Type

Investment Advisory

Font styles to use
Other font styles liked:
• font that is in logo

Requirements
Must have
• a very simple, but professional, elegant design. must include our color scheme, feel free to add other shades in our scheme.

```html
<!DOCTYPE html>
<html lang="en">
<head>
<meta charset="utf-8">
<title>Bulwark Aurelis — Presentation Slides, Part 01</title>
<link rel="stylesheet" href="https://fonts.googleapis.com/css2?family=Cinzel:wght@400;600&family=Didact+Gothic&family=Raleway:wght@400&display=swap">
<style>
  :root {
    --board: #ababab;
    --blue: #0a6fc2;
    --blue-band: rgba(10, 111, 194, 0.92);
    --ink: #2b2b2b;
    --white: #ffffff;
    --grey-band: #b3b3b3;
    --grey-bar: #6d6d6d;
    --rule: #bdbdbd;
    --serif: "Cinzel", serif;
    --sans: "Didact Gothic", sans-serif;
    --label: "Raleway", sans-serif;
  }
  * { box-sizing: border-box; margin: 0; padding: 0; }
  html, body { width: 1200px; height: 1127px; overflow: hidden; }
  body { background: var(--board); position: relative; font-family: var(--sans); color: var(--ink); }

  /* Company name placements: one font, one weight, one colour */
  .company { position: absolute; font-family: var(--sans); font-weight: 400; white-space: nowrap; line-height: 1; }
  .company--board { color: var(--white); font-size: 38px; }
  .company--top { left: 63px; top: 78px; }
  .company--bottom { left: 790px; top: 1040px; }

  .board-note { position: absolute; font-family: var(--label); color: var(--ink); }
  .features { left: 645px; top: 50px; font-size: 24px; line-height: 37px; }
  .part { left: 1020px; top: 50px; font-size: 33px; }
  .slide-label { font-size: 24px; width: 200px; text-align: right; }

  .slide { position: absolute; width: 520px; height: 292px; background: var(--white); overflow: hidden;
           box-shadow: 0 8px 18px rgba(0,0,0,0.28); }
  .slide--1 { left: 45px; top: 207px; }
  .slide--2 { left: 620px; top: 207px; }
  .slide--3 { left: 45px; top: 633px; }
  .slide--4 { left: 620px; top: 633px; }
  .slide > * { position: absolute; }

  .title { font-family: var(--serif); font-size: 17px; letter-spacing: 0.03em; font-weight: 400; white-space: nowrap; }
  .band { height: 39px; top: 17px; left: 0; right: 0; background: var(--blue-band); }
  .band .title { color: var(--white); position: absolute; left: 19px; top: 9px; }

  .mini-company { font-family: var(--sans); color: var(--blue); font-size: 9px; white-space: nowrap; }

  .footer-rule { height: 2px; background: var(--rule); left: 0; }

  .heading { font-family: var(--serif); font-weight: 600; font-size: 7.5px; color: var(--blue); letter-spacing: 0.03em; }
  .copy { font-size: 7px; line-height: 10px; color: var(--ink); }

  /* Slide 1 */
  .cover-photo { inset: 0; background:
      linear-gradient(120deg, #2a2a2a 0%, #d8d8d8 18%, #ffffff 45%, #f0f0f0 55%, #8a8a8a 75%, #2d2d2d 100%); }
  .company--cover { left: 9px; top: 46px; color: var(--blue); font-size: 30px; }
  .cover-motto { left: 261px; top: 274px; font-size: 7.5px; color: var(--ink); white-space: nowrap; }

  /* Slide 2 */
  .members-photo { left: 269px; top: 0; width: 239px; height: 248px;
      background: linear-gradient(180deg, #d9d9d9 0%, #9c9c9c 45%, #2d2d2d 100%); }
  .slide--2 .band { z-index: 2; }
  .member { left: 53px; }
  .member--1 { top: 94px; }
  .member--2 { top: 184px; }
  .member__name { font-family: var(--serif); font-weight: 600; font-size: 12px; color: var(--blue); line-height: 14px; }
  .member .copy { font-size: 8.5px; line-height: 10.5px; }
  .office { left: 335px; top: 145px; width: 163px; height: 94px; background: var(--blue); color: var(--white);
            padding: 24px 0 0 12px; font-size: 7.8px; line-height: 11px; white-space: nowrap; }
  .office strong { font-family: var(--serif); font-weight: 600; font-size: 8px; display: block; }
  .slide--2 .footer-rule, .slide--4 .footer-rule { top: 275px; width: 421px; }
  .slide--2 .mini-company, .slide--4 .mini-company { left: 430px; top: 268px; }

  /* Slide 3 */
  .overview-band { left: 13px; right: 0; top: 10px; height: 39px; background: var(--grey-band); }
  .overview-band .title { position: absolute; left: 9px; top: 10px; color: #1f1f1f; }
  .side-bar { left: 0; top: 0; width: 13px; height: 230px; background: var(--grey-bar); }
  .overview-photo { left: 0; top: 55px; width: 272px; height: 237px;
      clip-path: polygon(0 0, 221px 0, 272px 100%, 0 100%);
      background: linear-gradient(160deg, #3a3a3a 0%, #cfcfcf 40%, #f4f4f4 60%, #7b7b7b 100%); }
  .team-box { left: 43px; top: 177px; width: 163px; height: 93px; background: rgba(90,90,90,0.92);
              color: var(--white); padding: 13px 0 0 12px; }
  .team-box .heading { color: var(--white); }
  .team-box .copy { color: var(--white); margin-top: 9px; }
  .team-box ul { list-style: none; margin-top: 6px; font-family: var(--serif); font-size: 7.5px; line-height: 10px; color: var(--white); }
  .strategy { left: 272px; top: 64px; width: 125px; }
  .core { left: 353px; top: 182px; width: 135px; }
  .strategy .copy, .core .copy { margin-top: 12px; }
  .slide--3 .mini-company { left: 433px; top: 61px; }
  .blue-rule { left: 510px; top: 88px; width: 2px; height: 204px; background: var(--blue); }

  /* Slide 4 */
  .slide--4 .title { font-size: 18px; left: 24px; top: 8px; }
  .advantage-bar { left: 0; top: 73px; width: 13px; height: 165px; background: var(--grey-bar); }
  .adv-block { left: 27px; width: 200px; }
  .adv-block--1 { top: 74px; }
  .adv-block--2 { top: 189px; }
  .adv-block .copy { margin-top: 12px; }
  .adv-rule { left: 13px; top: 155px; width: 215px; height: 2px; background: var(--blue); }
  .principles-photo { left: 230px; top: 54px; width: 275px; height: 203px;
      clip-path: polygon(15% 0, 100% 0, 100% 100%, 15% 100%, 0 50%);
      background: radial-gradient(circle at 65% 45%, #ffffff 0%, #e6e6e6 45%, #a9a9a9 100%); }
  .principles { left: 301px; top: 82px; width: 200px; }
  .principles .copy { font-size: 6.8px; line-height: 9.8px; margin-top: 10px; }
  .principles p + p { margin-top: 6px; }
</style>
</head>
<body>

  <p class="company company--board company--top">BULWARK AURELIS</p>

  <p class="board-note features">High Quality<br>100% Editable</p>
  <p class="board-note part">Part 01</p>

  <p class="board-note slide-label" style="left:352px; top:160px;">Slide 01</p>
  <p class="board-note slide-label" style="left:932px; top:160px;">Slide 02</p>
  <p class="board-note slide-label" style="left:356px; top:571px;">Slide 03</p>
  <p class="board-note slide-label" style="left:932px; top:571px;">Slide 04</p>

  <section class="slide slide--1">
    <div class="cover-photo" role="img" aria-label="Black and white photo looking up between glass skyscrapers"></div>
    <p class="company company--cover">BULWARK AURELIS</p>
    <p class="cover-motto">Prudence in Planning. Vigilance in Execution.</p>
  </section>

  <section class="slide slide--2">
    <div class="members-photo" role="img" aria-label="Black and white photo of a tall tower against the sky"></div>
    <div class="band"><h2 class="title">Managing Members</h2></div>
    <div class="member member--1">
      <h3 class="member__name">NATHAN R. ELLERY</h3>
      <p class="copy">Co-Founder &amp; Managing Member<br>Phone: 555.010.4821<br>Nathan@BulwarkAurelis.com</p>
    </div>
    <div class="member member--2">
      <h3 class="member__name">OWEN T. MARSH</h3>
      <p class="copy">Co-Founder &amp; Managing Member<br>Phone: 555.010.7390<br>Owen@BulwarkAurelis.com</p>
    </div>
    <div class="office">
      <strong>BULWARK AURELIS, LLC</strong>
      480 Harbor Row &nbsp;|&nbsp; Fairmont AL 35000<br>Office: 555.010.4821<br>BulwarkAurelis.com
    </div>
    <div class="footer-rule"></div>
    <p class="mini-company">BULWARK AURELIS</p>
  </section>

  <section class="slide slide--3">
    <div class="overview-band"><h2 class="title">Overview</h2></div>
    <div class="side-bar"></div>
    <div class="overview-photo" role="img" aria-label="Black and white photo of a modern office corridor with glass walls"></div>
    <div class="team-box">
      <h3 class="heading">MANAGEMENT TEAM</h3>
      <p class="copy">Veteran Business Owners &amp; Portfolio Manager.</p>
      <ul><li>· NATHAN R. ELLERY</li><li>· OWEN T. MARSH</li></ul>
    </div>
    <div class="strategy">
      <h3 class="heading">STRATEGY</h3>
      <p class="copy">Bulwark Aurelis, LLC seeks to take advantage of any Price-Value mismatch or Supply-Demand imbalance throughout the economy; ranging from economic industries and sectors, down to an individual business, security, or commodity.</p>
    </div>
    <div class="core">
      <h3 class="heading">CORE FOCUS</h3>
      <p class="copy">Undervalued/Overvalued securities, contracts, or other instruments; Looking for opportunities to capture significant value where intensive and proprietary fundamental, technical, and psychological research aligns with both established principles and sound logic.</p>
    </div>
    <p class="mini-company">BULWARK AURELIS</p>
    <div class="blue-rule"></div>
  </section>

  <section class="slide slide--4">
    <div class="band"><h2 class="title">Why Bulwark Aurelis? &nbsp;A Disciplined Advantage</h2></div>
    <div class="advantage-bar"></div>
    <div class="adv-block adv-block--1">
      <h3 class="heading">EXPERIENCED TEAM</h3>
      <p class="copy">Managing Members have more than 25 years combined experience across business management, financial markets, economics, research &amp; analytics.</p>
    </div>
    <div class="adv-rule"></div>
    <div class="adv-block adv-block--2">
      <h3 class="heading">DISCIPLINED PROCESS</h3>
      <p class="copy">We follow a disciplined process based on established principles and sound logic in accordance with the scientific method.</p>
    </div>
    <div class="principles-photo" role="img" aria-label="Soft grey photo of a domed glass ceiling"></div>
    <div class="principles">
      <h3 class="heading">METHODICAL APPLICATION<br>OF KNOWLEDGE AND EXPERIENCE</h3>
      <div class="copy">
        <p><b>Josiah Whitcomb and Arthur Pennick</b> respectively provide the description of our operating principles.</p>
        <p>“Industry and Patience are the Surest Means to Plenty.”</p>
        <p>“An Investment in Knowledge Always Pays the Best Interest.”</p>
        <p>“Risk Comes from not Knowing What You are Doing.”</p>
        <p>“Investment is most Intelligent when it’s most Business-Like.”</p>
        <p>“Know What You are Doing; Know Your Business.”</p>
      </div>
    </div>
    <div class="footer-rule"></div>
    <p class="mini-company">BULWARK AURELIS</p>
  </section>

  <p class="company company--board company--bottom">BULWARK AURELIS</p>

</body>
</html>
```